Corvell Tiling Solutions, QBCC 8471302, ABN 48290517736, Email corvelltiling@brindlemail.com,Mobile 04958142

Corvell Tiling Solutions, is the name of my wall and floor tiling company and the details above are needed on the business card. Im open to see what people come up with i really have no colour requirements or other design specs as long as its not too plain.

```html
<!DOCTYPE html>
<html lang="en">
<head>
<meta charset="utf-8">
<title>Corvell Tiling Solutions – Business Card</title>
<link href="https://fonts.googleapis.com/css2?family=Exo+2:wght@300;400;500;600&display=swap" rel="stylesheet">
<style>
  :root {
    --bg: #e4e4e4;
    --charcoal: #2b2b2b;
    --paper: #ffffff;
    --orange: #ee6a12;
    --orange-light: #f5871f;
    --red: #d8232a;
    --red-dark: #b9161d;
    --mist: #e2e2e2;
    --ink: #3a3a3a;
    --ink-soft: #6a6a6a;
    --white: #ffffff;
  }
  * { box-sizing: border-box; margin: 0; padding: 0; }
  html, body {
    width: 1200px; height: 907px; overflow: hidden;
    background: var(--bg);
    font-family: "Exo 2", "Titillium Web", sans-serif;
  }
  .canvas {
    position: relative; width: 1200px; height: 907px;
    display: flex; justify-content: center; align-items: center; gap: 100px;
  }
  .card {
    position: relative; width: 340px; height: 595px;
    display: flex; flex-direction: column;
    background: var(--paper);
    box-shadow: 0 14px 30px rgba(0,0,0,.18);
    overflow: hidden;
  }
  .band { display: flex; flex-direction: column; justify-content: center; align-items: center; }
  .band--charcoal { background: var(--charcoal); color: var(--white); }
  .band--paper { background: var(--paper); }
  .band--orange { background: linear-gradient(135deg, var(--orange-light), var(--orange)); color: var(--white); }
  .band--red { background: linear-gradient(135deg, var(--red), var(--red-dark)); color: var(--white); }
  .band--mist { background: var(--mist); color: var(--ink); }

  /* Front */
  .front .band--charcoal { height: 120px; }
  .front .band--paper { flex: 1; }
  .front .band--orange { height: 145px; }
  .brand { display: flex; align-items: center; gap: 16px; }
  .brand__mark { width: 34px; height: 34px; background: var(--orange); flex: none; }
  .brand__name { font-weight: 300; font-size: 30px; line-height: 1.15; color: var(--ink); }
  .web { font-size: 15px; letter-spacing: .06em; }

  /* Back */
  .back .band--charcoal { height: 115px; }
  .back .band--paper { height: 120px; }
  .back .band--red { height: 100px; }
  .back .band--mist { height: 95px; }
  .back .band--orange { flex: 1; justify-content: flex-start; padding-top: 22px; }
  .person__name { font-size: 30px; font-weight: 400; letter-spacing: .06em; text-transform: uppercase; }
  .person__role { font-size: 11px; letter-spacing: .22em; text-transform: uppercase; margin-top: 4px; opacity: .85; }
  .back .brand__mark { width: 22px; height: 22px; }
  .back .brand__name { font-size: 20px; font-weight: 400; color: var(--orange); }
  .licence {
    margin-top: 12px; font-size: 12px; font-weight: 500;
    letter-spacing: .08em; color: var(--ink-soft); text-align: center;
  }
  .icon { width: 20px; height: 20px; margin-bottom: 8px; }
  .detail { font-size: 17px; letter-spacing: .05em; text-align: center; line-height: 1.35; }
  .detail--email { font-size: 16px; letter-spacing: .02em; }
  .web-bar {
    position: absolute; left: 30px; right: 30px; bottom: 22px; height: 34px;
    background: var(--charcoal); color: var(--white);
    display: flex; align-items: center; justify-content: center;
    font-size: 14px; letter-spacing: .12em;
  }
</style>
</head>
<body>
<main class="canvas">

  <section class="card front" aria-label="Card front">
    <div class="band band--charcoal"></div>
    <div class="band band--paper">
      <div class="brand">
        <span class="brand__mark"></span>
        <span class="brand__name">Corvell Tiling<br>Solutions</span>
      </div>
    </div>
    <div class="band band--orange">
      <p class="web">www.corvelltilingco.com</p>
    </div>
  </section>

  <section class="card back" aria-label="Card back">
    <div class="band band--charcoal">
      <p class="person__name">Dana Whitlock</p>
      <p class="person__role">General Manager</p>
    </div>
    <div class="band band--paper">
      <div class="brand">
        <span class="brand__mark"></span>
        <span class="brand__name">Corvell Tiling Solutions</span>
      </div>
      <p class="licence">QBCC 8471302 &nbsp;·&nbsp; ABN 48290517736</p>
    </div>
    <div class="band band--red">
      <svg class="icon" viewBox="0 0 24 24" aria-hidden="true"><path fill="#fff" d="M6.6 10.8a15 15 0 0 0 6.6 6.6l2.2-2.2a1 1 0 0 1 1-.25 11.4 11.4 0 0 0 3.6.57 1 1 0 0 1 1 1V20a1 1 0 0 1-1 1A17 17 0 0 1 3 4a1 1 0 0 1 1-1h3.5a1 1 0 0 1 1 1c0 1.25.2 2.45.57 3.57a1 1 0 0 1-.25 1z"/></svg>
      <p class="detail">04958142</p>
    </div>
    <div class="band band--mist">
      <svg class="icon" viewBox="0 0 24 24" aria-hidden="true"><rect x="2" y="5" width="20" height="14" fill="none" stroke="#3a3a3a" stroke-width="2"/><path d="M2 5l10 8 10-8" fill="none" stroke="#3a3a3a" stroke-width="2"/></svg>
      <p class="detail detail--email">corvelltiling@brindlemail.com</p>
    </div>
    <div class="band band--orange">
      <svg class="icon" viewBox="0 0 24 24" aria-hidden="true"><path fill="#fff" d="M12 2a7 7 0 0 0-7 7c0 5.2 7 13 7 13s7-7.8 7-13a7 7 0 0 0-7-7zm0 9.5A2.5 2.5 0 1 1 12 6.5a2.5 2.5 0 0 1 0 5z"/></svg>
      <p class="detail">42 Harlow Road<br>Unit 3, Brindle Street W.</p>
      <p class="web-bar">www.corvelltilingco.com</p>
    </div>
  </section>

</main>
</body>
</html>
```